Kestrel Signs Facebook Banner Design

Design a facebook banner for a sign company. I would like to have a modern approach to it.

Product Offering:
Signs
Banners
Decals
Commercial Wraps

```html
<!DOCTYPE html>
<html lang="en">
<head>
<meta charset="utf-8">
<title>Kestrel Signs – Facebook Cover</title>
<link rel="stylesheet" href="https://fonts.googleapis.com/css2?family=Exo+2:ital,wght@0,800;1,800&family=Poppins:ital,wght@0,400;1,400&display=swap">
<style>
  :root {
    --canvas: #5f686e;
    --paper: #ffffff;
    --brand-red: #e72f36;
    --brand-red-deep: #a8161c;
    --line-red: #d3141b;
    --charcoal: #454447;
    --photo-warm: #8a6f5c;
    --photo-cool: #4f7f99;
  }
  * { margin: 0; padding: 0; box-sizing: border-box; }
  html, body {
    width: 1200px;
    height: 1200px;
    overflow: hidden;
    background: var(--canvas);
  }
  .cover {
    position: absolute;
    left: 40px;
    top: 393px;
    width: 1120px;
    height: 414px;
    box-shadow: 0 14px 30px rgba(0,0,0,.35);
  }
  .cover svg { display: block; width: 100%; height: 100%; }
  .display { font-family: "Exo 2", sans-serif; font-weight: 800; font-style: italic; }
  .wordmark { font-family: "Exo 2", sans-serif; font-weight: 800; font-style: normal; }
  .script { font-family: "Poppins", sans-serif; font-style: italic; font-weight: 400; }
</style>
</head>
<body>
<section class="cover" aria-label="Kestrel Signs Facebook cover">
  <svg viewBox="0 0 1582 585" xmlns="http://www.w3.org/2000/svg">
    <defs>
      <linearGradient id="band-shade" x1="0" y1="0" x2="0" y2="1">
        <stop offset="0" stop-color="var(--brand-red)"/>
        <stop offset="0.45" stop-color="var(--brand-red)"/>
        <stop offset="1" stop-color="var(--brand-red-deep)"/>
      </linearGradient>
      <linearGradient id="photo-workshop" x1="0" y1="0" x2="1" y2="1">
        <stop offset="0" stop-color="var(--photo-cool)"/>
        <stop offset="0.6" stop-color="var(--photo-warm)"/>
        <stop offset="1" stop-color="#2f3438"/>
      </linearGradient>
      <linearGradient id="photo-press" x1="0" y1="0" x2="1" y2="1">
        <stop offset="0" stop-color="#8c9196"/>
        <stop offset="1" stop-color="#3c4248"/>
      </linearGradient>
      <clipPath id="red-field">
        <path d="M30,0 L1020,0 Q1300,185 1582,265 L1582,585 L1120,585 Q990,470 850,385 L520,140 Q300,40 30,0 Z"/>
      </clipPath>
    </defs>

    <rect class="paper" width="1582" height="585" fill="var(--paper)"/>

    <!-- accent sweeps -->
    <path class="sweep-charcoal" d="M1020,0 L1110,0 Q1330,190 1582,258 L1582,272 Q1290,200 1020,0 Z" fill="var(--charcoal)"/>
    <path class="sweep-line" d="M1110,0 Q1340,200 1582,262" fill="none" stroke="var(--line-red)" stroke-width="2"/>
    <path class="sweep-charcoal" d="M820,370 Q990,480 1085,585 L1150,585 Q1020,470 860,370 Z" fill="var(--charcoal)"/>
    <path class="sweep-line" d="M800,385 Q900,460 960,585" fill="none" stroke="var(--line-red)" stroke-width="3"/>
    <path class="sweep-charcoal" d="M80,15 Q250,55 370,112 L360,118 Q230,65 80,15 Z" fill="var(--charcoal)"/>
    <path class="sweep-line" d="M0,10 Q200,60 330,145" fill="none" stroke="var(--line-red)" stroke-width="1.2"/>

    <!-- red field with service bands -->
    <g class="red-field" clip-path="url(#red-field)">
      <rect width="1582" height="585" fill="var(--brand-red)"/>
      <rect class="band" x="0" y="0" width="1582" height="150" fill="url(#band-shade)"/>
      <rect class="band" x="0" y="150" width="1582" height="112" fill="url(#band-shade)"/>
      <rect class="band" x="0" y="262" width="1582" height="123" fill="url(#band-shade)"/>
      <rect class="band" x="0" y="385" width="1582" height="200" fill="var(--brand-red)"/>
    </g>

    <!-- photo frames -->
    <g class="photo-frame">
      <circle cx="500" cy="224" r="176" fill="var(--paper)" stroke="var(--line-red)" stroke-width="2.5"/>
      <circle cx="500" cy="224" r="156" fill="url(#photo-workshop)" role="img" aria-label="Photo of a screen printer inspecting a print frame in a workshop"/>
    </g>
    <g class="photo-frame">
      <circle cx="737" cy="350" r="116" fill="var(--paper)" stroke="var(--line-red)" stroke-width="2.5"/>
      <circle cx="737" cy="350" r="100" fill="url(#photo-press)" role="img" aria-label="Photo of a technician operating a printing press"/>
    </g>

    <!-- welcome ribbon -->
    <text class="script" x="52" y="105" font-size="16" fill="#222">Welcome To</text>
    <path class="ribbon-tab" d="M0,118 L22,118 L35,148 L0,148 Z" fill="var(--charcoal)"/>
    <path class="ribbon" d="M25,118 L290,118 L322,148 L38,148 Z" fill="var(--brand-red)"/>
    <text class="script" x="52" y="140" font-size="21" fill="#fff">Kestrel Signs</text>

    <!-- headline -->
    <g class="headline display" font-size="60">
      <text x="57" y="235" fill="var(--brand-red)" textLength="222" lengthAdjust="spacingAndGlyphs">TOP SIGN</text>
      <text x="55" y="288" fill="var(--charcoal)" textLength="232" lengthAdjust="spacingAndGlyphs">DESIGN &amp;</text>
      <text x="55" y="342" fill="var(--charcoal)" textLength="233" lengthAdjust="spacingAndGlyphs">PRINTING</text>
      <text x="55" y="396" fill="var(--brand-red)" textLength="233" lengthAdjust="spacingAndGlyphs">EXPERTS</text>
    </g>

    <!-- services -->
    <g class="services display" font-size="56" fill="#fff">
      <text x="855" y="106" text-anchor="middle" textLength="148" lengthAdjust="spacingAndGlyphs">SIGNS</text>
      <text x="988" y="222" text-anchor="middle" textLength="226" lengthAdjust="spacingAndGlyphs">BANNERS</text>
      <text x="1072" y="336" text-anchor="middle" textLength="178" lengthAdjust="spacingAndGlyphs">DECALS</text>
      <text x="1130" y="455" textLength="318" lengthAdjust="spacingAndGlyphs">COMMERCIAL</text>
      <text x="1132" y="514" textLength="172" lengthAdjust="spacingAndGlyphs">WRAPS</text>
    </g>

    <!-- brand name -->
    <g class="wordmark" fill="var(--brand-red)" text-anchor="middle">
      <text x="1400" y="86" font-size="38">KESTREL</text>
      <text x="1400" y="118" font-size="30">SIGNS</text>
    </g>
  </svg>
</section>
</body>
</html>
```